Eye catching Bottle label for pink gin targeting women 25+

We need a new label for a re-launch of our Glimmering Wildberry pink gin liqueur. We would like it to look premium and eye catching on the shelf. We have 2 labels we require, one for 200ml bottle (2x2 inches) and one for 500ml bottle 4x4 inches). Label must state the ml of the bottle abd that it is 18.75%Vol. Also say Glimmering Wildberry Gin Liqueur with the brand name at the top - Marlow Tide. We have a logo but it doesn't need to be used if it doesn't work with the design/colours. The gin is presented in a clear bottle and is pink and sparkly. See uploaded image for reference.

Target Market(s)

Women aged 25-45

Font styles to use
Decorative

Colors
f59296
fbd4d5
eea4c8

Requirements
Must have
• Bottle size - 500ml/200ml
• Must say 18.75% Vol
• Must have brand name - Marlow Tide
• Must have product name - Shimmering Pink Strawberry
• Must say - Gin Liqueur
Nice to have
• Some sort of floral or swirley background detail would be nice
Should not have
• Must not appeal to children

```html
<!DOCTYPE html>
<html lang="en">
<head>
<meta charset="utf-8">
<title>Marlow Tide – Glimmering Wildberry Pink Gin Liqueur Label</title>
<link rel="stylesheet" href="https://fonts.googleapis.com/css2?family=Oswald:wght@500&family=Open+Sans:wght@700&family=Playfair+Display:wght@400;700&family=Josefin+Sans:wght@400&display=swap">
<style>
  :root {
    --backdrop: #f4f1f2;
    --label-white: #ffffff;
    --rose: #e9457f;
    --rose-soft: #f59296;
    --blush: #fbd4d5;
    --orchid: #eea4c8;
    --slate: #6e6e6e;
    --ink: #1f1f1f;
  }
  * { margin: 0; padding: 0; box-sizing: border-box; }
  html, body {
    width: 867px;
    height: 1200px;
    overflow: hidden;
    background: var(--backdrop);
  }
  .label {
    position: absolute;
    left: 33px;
    top: 195px;
    width: 800px;
    height: 810px;
    background: var(--label-white);
    box-shadow: 0 4px 18px rgba(0,0,0,0.08);
    overflow: hidden;
  }
  .pattern-strip {
    position: absolute;
    left: 0;
    top: 0;
    width: 280px;
    height: 100%;
    background: linear-gradient(160deg, var(--rose-soft) 0%, var(--orchid) 45%, var(--blush) 100%);
  }
  .info {
    position: absolute;
    left: 280px;
    top: 0;
    width: 370px;
    height: 100%;
    text-align: center;
    color: var(--ink);
  }
  .info > * {
    position: absolute;
    left: 0;
    right: 0;
  }
  .brand {
    top: 108px;
    display: flex;
    align-items: center;
    justify-content: center;
    gap: 10px;
    font-family: "Open Sans", Arial, sans-serif;
    font-weight: 700;
    font-size: 24px;
    line-height: 1;
    letter-spacing: 1px;
    color: var(--ink);
  }
  .brand-dot {
    width: 14px;
    height: 14px;
    border-radius: 50%;
    background: var(--rose);
  }
  .product-name {
    top: 250px;
    font-family: "Oswald", "Arial Narrow", sans-serif;
    font-weight: 500;
    font-size: 62px;
    line-height: 1;
    letter-spacing: 1px;
    color: var(--rose);
  }
  .product-flavour {
    top: 326px;
    font-family: "Open Sans", Arial, sans-serif;
    font-weight: 700;
    font-size: 30px;
    line-height: 1;
    letter-spacing: 1px;
    color: var(--slate);
  }
  .variant {
    top: 390px;
    padding-right: 110px;
    font-family: "Playfair Display", Georgia, serif;
    font-weight: 400;
    font-size: 56px;
    line-height: 1;
    color: var(--rose);
  }
  .spirit {
    top: 440px;
    font-family: "Playfair Display", Georgia, serif;
    font-weight: 700;
    font-size: 118px;
    line-height: 1;
    letter-spacing: 2px;
    color: var(--ink);
  }
  .category {
    top: 572px;
    display: flex;
    align-items: center;
    justify-content: center;
    gap: 10px;
    font-family: "Josefin Sans", Arial, sans-serif;
    font-size: 19px;
    letter-spacing: 5px;
    color: var(--ink);
  }
  .category::before,
  .category::after {
    content: "";
    width: 38px;
    height: 2px;
    background: var(--ink);
  }
  .volume,
  .strength {
    font-family: "Open Sans", Arial, sans-serif;
    font-weight: 700;
    font-size: 26px;
    line-height: 1;
    color: var(--ink);
  }
  .volume { top: 705px; }
  .strength { top: 745px; }
</style>
</head>
<body>
  <main class="label">
    <div class="pattern-strip" role="img" aria-label="Decorative pattern of pink berries and swirls"></div>
    <section class="info">
      <div class="brand"><span class="brand-dot"></span><span>Marlow Tide</span></div>
      <h1 class="product-name">GLIMMERING</h1>
      <p class="product-flavour">WILDBERRY</p>
      <p class="variant">pink</p>
      <p class="spirit">GIN</p>
      <p class="category">LIQUEUR</p>
      <p class="volume">500ml</p>
      <p class="strength">18.75%Vol</p>
    </section>
  </main>
</body>
</html>
```